Venture Keystone - Client Appreciation Party Invitation and Poster

We need a printable invitation, a version of the same invitation that can be emailed out, and also a Poster of the invitation for our annual client appreciation party.

The location is called: The Lanternhouse. Here is a link to the location: https://www.thelanternhousevenue.example/

We like their font and their little logo that you see when you log onto this page. But we'd love to see creatively what you can come up with.

This party is for our clients who are interior designers and owners in the Hospitality industry. Here are the details which need to be included in the invitation:

Location: The Lanternhouse - 482 W Brindle Ave. Chicago IL 60614
Date/Time: Thursday August 23rd - 5:30-9:00pm
RSVP: Please RSVP to: gathering@venturekeystone.example

Then our Sponsors Logos need to be included on the bottom: I have uploaded those logos here as well as our Logo and a copy of the invitation we did for last year's party so you can see sort of what we've done in the past.

For the poster - we typically do a version of the invitation (see uploaded example of last year's poster) with the sponsor logos and the overall theme of the invitation just a bit simplified by removing the date/time/location info. We need this in a printable format which can be blown up to a 24x30 poster size.

Requirements
Must have
• use 2 to 3 colors only.
• logos of sponsors can be of the same color.

```html
<!DOCTYPE html>
<html lang="en">
<head>
<meta charset="utf-8">
<title>Venture Keystone – Client Appreciation Party</title>
<link rel="stylesheet" href="https://fonts.googleapis.com/css2?family=Cormorant+Garamond:wght@500;600;700&family=Kaushan+Script&display=swap">
<style>
  :root {
    --backdrop: #e9e4e5;
    --paper: #ffffff;
    --blush-light: #fbe3e8;
    --blush: #f4b9c5;
    --blush-deep: #e9a3b2;
    --berry: #9c3e4f;
    --rose: #e64a66;
    --ink: #33262a;
    --frame-line: #ffffff;
  }
  * { margin: 0; padding: 0; box-sizing: border-box; }
  html, body {
    width: 1200px; height: 1200px; overflow: hidden;
    background: var(--backdrop);
    font-family: "Cormorant Garamond", Georgia, serif;
  }
  .invitation {
    position: absolute; left: 150px; top: 39px;
    width: 900px; height: 1122px;
    background: var(--paper);
  }
  .invitation__field {
    position: absolute; left: 14px; top: 25px;
    width: 873px; height: 1027px;
    background: radial-gradient(ellipse at 52% 52%, var(--blush-light) 0%, #f8cdd6 45%, var(--blush) 100%);
    overflow: hidden;
  }
  .flourish { position: absolute; }
  .flourish--top-left {
    left: 0; top: 0; width: 310px; height: 330px;
    background: radial-gradient(ellipse at 20% 25%, rgba(233,150,168,.75) 0%, rgba(233,150,168,.35) 45%, rgba(233,150,168,0) 72%);
  }
  .flourish--top-right {
    right: 0; top: 0; width: 160px; height: 320px;
    background: radial-gradient(ellipse at 75% 40%, rgba(255,255,255,.9) 0%, rgba(255,255,255,.45) 50%, rgba(255,255,255,0) 78%);
  }
  .flourish--bottom-left {
    left: 0; bottom: 0; width: 190px; height: 200px;
    background: radial-gradient(ellipse at 30% 70%, rgba(255,255,255,.75) 0%, rgba(255,255,255,.3) 50%, rgba(255,255,255,0) 78%);
  }
  .frame-lines { position: absolute; left: 0; top: 0; width: 900px; height: 1122px; }

  .headline { position: absolute; left: 0; top: 0; width: 900px; height: 470px; }
  .headline__save,
  .headline__date {
    position: absolute; font-family: "Kaushan Script", "Brush Script MT", cursive;
    font-weight: 400; line-height: 1; white-space: nowrap;
  }
  .headline__save {
    left: 140px; top: 118px; font-size: 245px; color: var(--paper);
    text-shadow: 0 4px 10px rgba(156,62,79,.25);
    letter-spacing: -4px;
  }
  .headline__date {
    left: 372px; top: 330px; font-size: 96px; color: var(--berry);
  }

  .line {
    position: absolute; left: 0; width: 900px;
    text-align: center; line-height: 1; white-space: nowrap;
  }
  .lining { font-variant-numeric: lining-nums; font-feature-settings: "lnum" 1; }
  .eyebrow { top: 91px; font-size: 25px; font-weight: 600; color: var(--berry); letter-spacing: .5px; }
  .invite-lead { top: 518px; font-size: 36px; font-weight: 600; color: var(--berry); letter-spacing: .5px; }
  .divider {
    position: absolute; left: 423px; width: 54px; height: 6px;
    background: var(--blush-deep); border-radius: 3px;
  }
  .divider--upper { top: 583px; }
  .divider--lower { top: 801px; }
  .event-date { top: 612px; font-size: 78px; font-weight: 600; color: var(--rose); }
  .event-day { top: 693px; font-size: 35px; font-weight: 600; color: var(--ink); letter-spacing: 14px; padding-left: 14px; }
  .event-time { top: 734px; font-size: 45px; font-weight: 500; color: var(--ink); }
  .venue-name { top: 832px; font-size: 48px; font-weight: 700; color: var(--berry); letter-spacing: .5px; }
  .venue-address { top: 893px; font-size: 29px; font-weight: 500; color: var(--berry); }
  .rsvp-label { top: 951px; font-size: 27px; font-weight: 500; color: var(--ink); }
  .rsvp-email { top: 985px; font-size: 23px; font-weight: 500; color: var(--berry); }
  .sponsors {
    position: absolute; left: 0; top: 1072px; width: 900px; height: 30px;
    display: flex; justify-content: center; align-items: center; gap: 26px;
  }
  .sponsor {
    display: flex; align-items: center; gap: 6px;
    font-size: 17px; font-weight: 600; color: var(--berry); white-space: nowrap;
  }
  .sponsor__mark { width: 12px; height: 12px; background: var(--berry); }
</style>
</head>
<body>
  <main class="invitation">
    <div class="invitation__field">
      <div class="flourish flourish--top-left" role="img" aria-label="Rose-toned floral scroll ornament in the top left corner"></div>
      <div class="flourish flourish--top-right" role="img" aria-label="White floral scroll ornament in the top right corner"></div>
      <div class="flourish flourish--bottom-left" role="img" aria-label="White floral scroll ornament in the bottom left corner"></div>
    </div>

    <svg class="frame-lines" viewBox="0 0 900 1122" aria-hidden="true">
      <g stroke="var(--frame-line)" stroke-width="1.5" fill="none">
        <line x1="35" y1="44" x2="473" y2="44"/>
        <line x1="35" y1="44" x2="35" y2="772"/>
        <line x1="865" y1="424" x2="865" y2="1052"/>
      </g>
      <rect x="168" y="168" width="588" height="290" fill="none" stroke="var(--berry)" stroke-width="2.5"/>
    </svg>

    <h2 class="headline">
      <span class="headline__save">Save</span>
      <span class="headline__date">The Date</span>
    </h2>

    <p class="line eyebrow">ANNUAL CLIENT APPRECIATION PARTY</p>
    <p class="line invite-lead">PLEASE JOIN US FOR A DINNER</p>
    <div class="divider divider--upper" role="img" aria-label="Small floral divider ornament"></div>
    <p class="line event-date lining">23.8.2018</p>
    <p class="line event-day">THURSDAY</p>
    <p class="line event-time lining">5:30 TO 9:00PM</p>
    <div class="divider divider--lower" role="img" aria-label="Small floral divider ornament"></div>
    <h1 class="line venue-name">THE LANTERNHOUSE</h1>
    <p class="line venue-address">482 W Brindle Ave. Chicago IL 60614</p>
    <p class="line rsvp-label">Please RSVP to</p>
    <p class="line rsvp-email">gathering@venturekeystone.example</p>

    <footer class="sponsors">
      <span class="sponsor"><span class="sponsor__mark"></span>Marlow Trade</span>
      <span class="sponsor">Vesper Form</span>
      <span class="sponsor">Holloway Seating</span>
      <span class="sponsor"><span class="sponsor__mark"></span>Dune Interiors</span>
      <span class="sponsor">Brightmark Lighting</span>
      <span class="sponsor">Signet Fabrics</span>
    </footer>
  </main>
</body>
</html>
```